Copperleaf Motorized Shade Business Card

Hello, we've had our logo made. Now we are looking for a clean and cool looking business card. One side can just be the logo with any design elements that might look good with it. The other side will be Name, Phone Number and Email. There will not be an address on the card.

```html
<!DOCTYPE html>
<html lang="en">
<head>
<meta charset="utf-8">
<title>Copperleaf Motorized Shade – Business Card</title>
<link rel="stylesheet" href="https://fonts.googleapis.com/css2?family=Bebas+Neue&family=Montserrat:wght@500&display=swap">
<style>
  :root {
    --backdrop: #2b5283;
    --card: #ffffff;
    --navy: #284a7c;
    --sky: #22aee6;
    --stripe-tint: #eaf6fc;
    --divider: #e4e8ee;
  }
  * { margin: 0; padding: 0; box-sizing: border-box; }
  html, body { width: 1200px; height: 1199px; overflow: hidden; }
  body {
    background: var(--backdrop);
    position: relative;
    font-family: "Bebas Neue", "Arial Narrow", sans-serif;
  }
  .card {
    position: absolute;
    left: 350px;
    width: 499px;
    height: 312px;
    background: var(--card);
  }
  .card--front { top: 260px; }
  .card--back { top: 630px; }

  .pattern-fill {
    position: absolute;
    inset: 0;
    background: var(--stripe-tint);
  }

  .brand {
    position: absolute;
    display: flex;
    align-items: center;
    gap: 12px;
    color: var(--navy);
    text-transform: uppercase;
    line-height: 0.95;
  }
  .brand__mark {
    flex: none;
    background: var(--navy);
  }
  .card--front .brand {
    left: 50%;
    top: 50%;
    transform: translate(-50%, -50%);
    font-size: 54px;
  }
  .card--front .brand__mark { width: 40px; height: 40px; }
  .card--back .brand {
    left: 124px;
    top: 156px;
    transform: translate(-50%, -50%);
    font-size: 34px;
    gap: 8px;
  }
  .card--back .brand__mark { width: 24px; height: 24px; }

  .divider {
    position: absolute;
    left: 248px;
    top: 46px;
    width: 2px;
    height: 220px;
    background: var(--divider);
  }

  .contact {
    position: absolute;
    left: 270px;
    top: 70px;
    color: var(--navy);
  }
  .contact__name {
    font-size: 50px;
    letter-spacing: 1px;
    margin-left: 18px;
    line-height: 1;
    font-weight: 400;
  }
  .contact__list { list-style: none; margin-top: 34px; }
  .contact__item {
    display: flex;
    align-items: center;
    gap: 12px;
    font-size: 16px;
    letter-spacing: 0.5px;
    height: 32px;
    margin-bottom: 12px;
  }
  .contact__icon { width: 30px; height: 30px; flex: none; }
</style>
</head>
<body>

  <section class="card card--front" aria-label="Business card front">
    <div class="pattern-fill" role="img" aria-label="Light blue diagonal stripe pattern"></div>
    <div class="brand">
      <span class="brand__mark"></span>
      <span class="brand__name">Copperleaf<br>Motorized Shade</span>
    </div>
  </section>

  <section class="card card--back" aria-label="Business card back">
    <div class="brand">
      <span class="brand__mark"></span>
      <span class="brand__name">Copperleaf<br>Motorized Shade</span>
    </div>
    <div class="divider"></div>
    <div class="contact">
      <h1 class="contact__name">Marcus Hale</h1>
      <ul class="contact__list">
        <li class="contact__item">
          <svg class="contact__icon" viewBox="0 0 30 30" aria-hidden="true">
            <rect x="8" y="2" width="14" height="26" rx="2.5" fill="none" stroke="var(--navy)" stroke-width="2"/>
            <line x1="8" y1="6.5" x2="22" y2="6.5" stroke="var(--navy)" stroke-width="1.5"/>
            <line x1="8" y1="23.5" x2="22" y2="23.5" stroke="var(--navy)" stroke-width="1.5"/>
          </svg>
          <span>210-555-0143</span>
        </li>
        <li class="contact__item">
          <svg class="contact__icon" viewBox="0 0 30 30" aria-hidden="true">
            <circle cx="15" cy="15" r="12.5" fill="var(--navy)"/>
            <g fill="none" stroke="#fff" stroke-width="1.4">
              <ellipse cx="15" cy="15" rx="5" ry="12"/>
              <line x1="15" y1="3" x2="15" y2="27"/>
              <line x1="3" y1="15" x2="27" y2="15"/>
              <path d="M5 9h20M5 21h20"/>
            </g>
          </svg>
          <span>MHALE_CEO@COPPERLEAF.CO</span>
        </li>
      </ul>
    </div>
  </section>

</body>
</html>
```